Communication and Marketing agency needs a new presentation card

We are a group of communication and marketing agencies specialized in companies that are in the logistics and industrial sector. The head agency is VELUNEX Grupo and the group consists of 4 agencies: VELUNEX Media, VELUNEX Digital, VELUNEX Research and PlanoDeImagenes. We hace 4 offices in Spain (Madrid, Barcelona, Valencia and Murcia). We are looking for a clean and attractive design that transmits our experience, brand presence in the market and knowledge to those who receive the card.It has to maintain the colors of the logo that is attached.
logistics and industrial sector
Marketing department
Clean and attractive design

```html
<!DOCTYPE html>
<html lang="es">
<head>
<meta charset="utf-8">
<title>VELUNEX Grupo — Tarjeta de presentación</title>
<link rel="stylesheet" href="https://fonts.googleapis.com/css2?family=Mulish:wght@400;600;700&display=swap">
<style>
  :root {
    --brand-red: #b01e24;
    --ink: #2b2b2d;
    --band-grey: #505052;
    --soft-grey: #8a8a8c;
    --card-white: #f7f7f7;
    --map-grey: #dcdcdc;
    --backdrop: #e6e6e6;
  }
  * { box-sizing: border-box; margin: 0; padding: 0; }
  html, body {
    width: 1200px; height: 960px; overflow: hidden;
    background: var(--backdrop);
    font-family: "Mulish", sans-serif;
    color: var(--ink);
  }
  .stage {
    position: relative; width: 1200px; height: 960px;
  }
  .card {
    position: absolute; left: 280px;
    width: 640px; height: 376px;
    background: var(--card-white);
    box-shadow: 0 6px 24px rgba(0,0,0,.12);
    overflow: hidden;
  }
  .card--front { top: 76px; }
  .card--back { top: 508px; }

  /* Front side */
  .contact { position: absolute; left: 48px; top: 62px; }
  .contact__name { font-size: 21px; font-weight: 400; letter-spacing: .5px; }
  .contact__role { font-size: 15px; color: var(--brand-red); letter-spacing: .4px; margin-top: 2px; }
  .contact__rule { width: 34px; height: 1px; background: var(--soft-grey); margin: 9px 0 12px; }
  .contact__row { display: flex; align-items: flex-start; gap: 12px; font-size: 14px; line-height: 19px; margin-bottom: 6px; }
  .contact__icon { flex: none; width: 18px; height: 18px; margin-top: 1px; }

  .brand-lockup {
    position: absolute; right: 36px; top: 58px;
    font-size: 38px; font-weight: 700; color: var(--brand-red);
    letter-spacing: 1px; text-align: right; line-height: 1;
  }
  .agencies {
    position: absolute; right: 36px; top: 136px;
    display: flex; gap: 24px; align-items: flex-end;
  }
  .agency { font-size: 12px; font-weight: 600; letter-spacing: .3px; color: var(--soft-grey); }
  .agency--red { color: var(--brand-red); }

  .tagline {
    position: absolute; left: 264px; top: 258px;
    font-size: 10.5px; font-weight: 600; color: var(--brand-red); letter-spacing: .2px;
  }
  .band {
    position: absolute; display: flex; align-items: center;
    color: #fff; font-size: 13px; letter-spacing: .8px;
  }
  .band--services { left: 0; top: 244px; width: 240px; height: 54px; background: var(--band-grey); padding-left: 24px; font-size: 12px; }
  .band--offices { left: 252px; top: 280px; right: 0; height: 64px; background: var(--brand-red); padding-left: 22px; font-size: 14px; }

  /* Back side */
  .world-map {
    position: absolute; left: 100px; top: 60px; width: 440px; height: 250px;
    background: radial-gradient(ellipse at center, var(--map-grey) 0%, rgba(220,220,220,.5) 55%, rgba(220,220,220,0) 75%);
  }
  .back-lockup {
    position: absolute; left: 0; right: 0; top: 160px;
    text-align: center; font-size: 44px; font-weight: 700;
    color: var(--brand-red); letter-spacing: 1.5px;
  }
</style>
</head>
<body>
<main class="stage">

  <section class="card card--front" aria-label="Anverso de la tarjeta">
    <div class="contact">
      <p class="contact__name">MARTÍN OLMEDO</p>
      <p class="contact__role">DIRECTOR MADRID</p>
      <div class="contact__rule"></div>
      <div class="contact__row">
        <svg class="contact__icon" viewBox="0 0 18 18" aria-hidden="true">
          <circle cx="9" cy="9" r="9" fill="var(--brand-red)"/>
          <path d="M6.3 4.6c.4-.3.9-.2 1.1.2l.8 1.5c.2.4.1.8-.2 1.1l-.6.5c.5 1.1 1.3 1.9 2.4 2.4l.5-.6c.3-.3.7-.4 1.1-.2l1.5.8c.4.2.5.7.2 1.1l-.7.9c-.4.5-1.1.6-1.7.4-2.4-.9-4.2-2.7-5.1-5.1-.2-.6-.1-1.3.4-1.7z" fill="#fff"/>
        </svg>
        <div>T. +34 910 407 215<br>M. +34 600 214 587</div>
      </div>
      <div class="contact__row">
        <svg class="contact__icon" viewBox="0 0 18 18" aria-hidden="true">
          <circle cx="9" cy="9" r="9" fill="var(--brand-red)"/>
          <rect x="4.5" y="6" width="9" height="6.5" fill="none" stroke="#fff" stroke-width="1.1"/>
          <path d="M4.5 6.2 9 9.8l4.5-3.6" fill="none" stroke="#fff" stroke-width="1.1"/>
        </svg>
        <div>molmedo@velunex.es</div>
      </div>
    </div>

    <p class="brand-lockup">VELUNEX Media</p>

    <div class="agencies">
      <span class="agency">VELUNEX Research</span>
      <span class="agency">VELUNEX Digital</span>
      <span class="agency agency--red">PlanoDeImagenes</span>
    </div>

    <p class="band band--services">MEDIA - DIGITAL - VIDEO - RESEARCH</p>
    <p class="tagline">Expertos en Marketing y Comunicación Logística e Industrial</p>
    <p class="band band--offices">MADRID - BARCELONA - VALENCIA - MURCIA</p>
  </section>

  <section class="card card--back" aria-label="Reverso de la tarjeta">
    <div class="world-map" role="img" aria-label="Mapa del mundo en gris suave como fondo decorativo"></div>
    <p class="back-lockup">VELUNEX Grupo</p>
  </section>

</main>
</body>
</html>
```